Education related business need name card design

We need name card design for long term study agent.
Company name is Harbor Lantern.
We support clients to connect to the world.
Clients are Japanese family who has primary and secondary school students.

Company Logo is reflection of the globe and HL (Harbor Lantern).
Since business is related to education, we would like to show reliability and love to see the world map (atlas) in the name card.

Target Market(s)

late 30's to 50's parents of primary and secondary students who are enthusiastic for education. Secondary school management

Industry/Entity Type

Education

Contact Information for Business Card

Company name, Address, Official position, Name, Phone number, Mobile number, email address,

Font styles to use
Serif
Other font styles liked:
• Century Gothic(logo)

Requirements
Must have
• Since businee is related to education, we would like to show reliability and love to see the world map (atlas) in the name card.

```html
<!DOCTYPE html>
<html lang="en">
<head>
<meta charset="utf-8">
<title>Harbor Lantern – Business Card</title>
<link href="https://fonts.googleapis.com/css2?family=Questrial&display=swap" rel="stylesheet">
<style>
  :root{
    --bg:#e9ebee;
    --white:#ffffff;
    --brand:#1b4f9e;
    --navy:#0d3a85;
    --blue-top:#1b9ad8;
    --blue-bottom:#0b55a6;
    --map-light:#cfe6f6;
    --map-mid:#9ccbea;
  }
  *{margin:0;padding:0;box-sizing:border-box}
  html,body{width:1200px;height:900px;overflow:hidden;background:var(--bg)}
  body{position:relative;font-family:"Questrial",sans-serif}
  .card{position:absolute;overflow:hidden;box-shadow:0 6px 18px rgba(0,0,0,.18)}
  .card-front{left:78px;top:34px;width:588px;height:363px;background:var(--white)}
  .card-back{left:388px;top:506px;width:566px;height:351px;
    background:linear-gradient(180deg,var(--blue-top) 0%,var(--blue-bottom) 100%)}

  .world-map{position:absolute;left:262px;top:31px;width:280px;height:150px;
    background:radial-gradient(ellipse at 50% 45%,var(--map-mid) 0%,var(--map-light) 60%,rgba(255,255,255,0) 100%);
    border-radius:40px}

  .brand{position:absolute;left:56px;top:66px;display:flex;align-items:center;gap:12px}
  .brand-mark{width:76px;height:76px;border-radius:50%;background:var(--brand)}
  .brand-name{color:var(--brand);font-size:24px;line-height:24px}

  .bands{position:absolute;left:0;top:176px;width:588px;height:187px}

  .person{position:absolute;right:328px;top:228px;text-align:right;color:var(--white)}
  .person-name{font-size:23px;font-weight:700;letter-spacing:.3px;line-height:26px}
  .person-role{font-size:16.5px;line-height:22px}
  .person-address{font-size:16.5px;line-height:23px;margin-top:8px}

  .contacts{position:absolute;left:298px;top:234px;list-style:none;color:var(--white);font-size:17px}
  .contacts li{display:flex;align-items:center;gap:8px;height:24.5px}
  .contacts svg{width:17px;height:17px;flex:none}

  .back-name{position:absolute;left:70px;top:222px;color:var(--white);font-size:38px;line-height:37px}
</style>
</head>
<body>

<section class="card card-front">
  <div class="world-map" role="img" aria-label="Dotted world map"></div>

  <div class="brand">
    <span class="brand-mark"></span>
    <div class="brand-name">Harbor<br>Lantern Pte.Ltd.</div>
  </div>

  <svg class="bands" viewBox="0 0 588 187" aria-hidden="true">
    <defs>
      <linearGradient id="frontBlue" x1="0" y1="0" x2="0" y2="1">
        <stop offset="0" stop-color="#1b9ad8"/>
        <stop offset="1" stop-color="#0b55a6"/>
      </linearGradient>
    </defs>
    <path d="M0 10 H395 L412 2 V0 H588 V187 H0 Z" fill="url(#frontBlue)"/>
    <path d="M414 0 H588 V4 H410 Z" fill="#1b9ad8"/>
    <path d="M0 10 H406 L384 35 H0 Z" fill="#0d3a85"/>
    <path d="M384 35 L406 10 L412 2" fill="none" stroke="#fff" stroke-width="2"/>
    <path d="M0 35 H384" stroke="#fff" stroke-width="2"/>
  </svg>

  <div class="person">
    <div class="person-name">Mei Tanaka</div>
    <div class="person-role">Managing Director</div>
    <div class="person-address">18, Quayside Lane<br>Country, 12345</div>
  </div>

  <ul class="contacts">
    <li><svg viewBox="0 0 17 17"><rect width="17" height="17" rx="3" fill="#fff"/><path d="M4 7c0-2 2-3 4.5-3S13 5 13 7l-2 .5-.5-1.5h-4L6 7.5Zm1 1h7l1 5H4Z" fill="#1579c4"/></svg>555-210-4418</li>
    <li><svg viewBox="0 0 17 17"><rect width="17" height="17" rx="3" fill="#fff"/><rect x="5.5" y="3" width="6" height="11" rx="1" fill="#1579c4"/><rect x="6.7" y="4.5" width="3.6" height="6" fill="#fff"/></svg>555-210-4419</li>
    <li><svg viewBox="0 0 17 17"><rect width="17" height="17" rx="3" fill="#fff"/><rect x="3.5" y="5" width="10" height="7" fill="none" stroke="#1579c4" stroke-width="1.4"/><path d="M3.5 5l5 4 5-4" fill="none" stroke="#1579c4" stroke-width="1.4"/></svg>hello@harborlantern.example</li>
    <li><svg viewBox="0 0 17 17"><rect width="17" height="17" rx="3" fill="#fff"/><path d="M7 10l3-3M6 8.5 4.8 9.7a1.8 1.8 0 0 0 2.5 2.5L8.5 11M11 8.5l1.2-1.2a1.8 1.8 0 0 0-2.5-2.5L8.5 6" fill="none" stroke="#1579c4" stroke-width="1.4" stroke-linecap="round"/></svg>www.harborlantern.example</li>
  </ul>
</section>

<section class="card card-back">
  <div class="back-name">Harbor<br>Lantern Pte.Ltd.</div>
</section>

</body>
</html>
```